new business venture [ self employed ] will register my business name as " LEARNOVA "
what I will offer is :-
computer lessons for new beginners.
Initial set up and basic overview.
lessons per hour in the comfort of your own home.
special rates for customers aged 50+
First lesson is half price with no obligation for booking any further appointments.
a learning and training plan will be presented based on your requirements.
an appraisal update on your new skills.

contact info:-
0161 4972015
07700 918342
grenwick@vellumail.net

```html
<!DOCTYPE html>
<html lang="en">
<head>
<meta charset="utf-8">
<title>LEARNOVA – Computer Tuition</title>
<link rel="stylesheet" href="https://fonts.googleapis.com/css2?family=Dancing+Script:wght@500&family=Great+Vibes&family=Oswald:wght@300&family=Josefin+Sans:wght@400&family=Roboto+Slab:wght@400&display=swap">
<style>
  :root {
    --sky-light: #dfe9ff;
    --sky-mid: #8aa4f2;
    --royal: #2a3fe0;
    --deep: #1226c9;
    --ink: #111111;
    --accent-red: #e8000b;
    --white: #ffffff;
    --frame: #c9d4ff;
  }
  html, body {
    margin: 0;
    padding: 0;
    overflow: hidden;
    background: var(--white);
  }
  .flyer {
    position: relative;
    width: 1200px;
    height: 850px;
    overflow: hidden;
    box-sizing: border-box;
    border: 14px solid var(--frame);
  }
  .flyer__backdrop {
    position: absolute;
    inset: 0;
    background:
      radial-gradient(ellipse at 78% 18%, var(--sky-light) 0%, rgba(223,233,255,0) 45%),
      linear-gradient(170deg, var(--sky-mid) 0%, var(--royal) 55%, var(--deep) 100%);
  }
  .brand {
    position: absolute;
    left: 180px;
    top: 40px;
    display: flex;
    align-items: center;
    gap: 34px;
  }
  .brand__mark {
    width: 150px;
    height: 150px;
    background: var(--accent-red);
  }
  .brand__name {
    font-family: "Dancing Script", cursive;
    font-weight: 500;
    font-size: 124px;
    line-height: 1;
    color: var(--ink);
    letter-spacing: 2px;
  }
  .headline {
    position: absolute;
    left: 0;
    top: 254px;
    width: 1200px;
    margin: 0;
    text-align: center;
    font-family: "Great Vibes", cursive;
    font-weight: 400;
    font-size: 68px;
    line-height: 1;
    color: var(--white);
  }
  .headline__rule {
    position: absolute;
    left: 92px;
    top: 326px;
    width: 1016px;
    height: 4px;
    background: var(--white);
  }
  .services {
    position: absolute;
    left: 0;
    top: 352px;
    width: 1200px;
    margin: 0;
    padding: 0;
    list-style: none;
    text-align: center;
    font-family: "Dancing Script", cursive;
    font-weight: 500;
    font-size: 38px;
    color: var(--ink);
  }
  .services__row {
    display: flex;
    justify-content: center;
    gap: 26px;
    height: 64px;
    align-items: center;
  }
  .services__item::before {
    content: "";
    display: inline-block;
    width: 16px;
    height: 16px;
    margin-right: 10px;
    border-radius: 50%;
    background: var(--accent-red);
    vertical-align: middle;
  }
  .offer {
    position: absolute;
    left: 0;
    top: 586px;
    width: 1200px;
    text-align: center;
    font-family: "Oswald", sans-serif;
    font-weight: 300;
    font-size: 30px;
    color: var(--white);
  }
  .contact__phones {
    position: absolute;
    left: 0;
    top: 700px;
    width: 1200px;
    display: flex;
    justify-content: center;
    gap: 50px;
    font-family: "Josefin Sans", sans-serif;
    font-size: 54px;
    color: var(--white);
  }
  .contact__email {
    position: absolute;
    left: 0;
    top: 758px;
    width: 1200px;
    text-align: center;
    font-family: "Roboto Slab", serif;
    font-size: 56px;
    color: var(--white);
  }
</style>
</head>
<body>
  <main class="flyer">
    <div class="flyer__backdrop" role="img" aria-label="Blue background with a curving perspective grid of light dots and rounded squares"></div>

    <header class="brand">
      <div class="brand__mark"></div>
      <span class="brand__name">LEARNOVA</span>
    </header>

    <h1 class="headline">Offering Computer Tutition</h1>
    <div class="headline__rule"></div>

    <ul class="services">
      <li class="services__row">
        <span class="services__item">Beginner lessons</span>
        <span class="services__item">Setup and Overview</span>
        <span class="services__item">In your own home</span>
      </li>
      <li class="services__row">
        <span class="services__item">Customised training plans</span>
        <span class="services__item">Skill Appraisells</span>
      </li>
      <li class="services__row">
        <span class="services__item">Special rates for customers aged 50+</span>
      </li>
    </ul>

    <p class="offer">1st Lesson Half Price and Obligation Free</p>

    <div class="contact__phones">
      <span class="contact__phone">07700 918342</span>
      <span class="contact__phone">0161 4972015</span>
    </div>
    <div class="contact__email">grenwick@vellumail.net</div>
  </main>
</body>
</html>
```